Website redesign

PLOBrisk.com is a website that allows real estate investors to search for and find investment grade residential real estate property. The website is up and running, but is in desperate need of a facelift. You can see the existing website at http://www.plobrisk.example. PLO stands for "Real Estate Investor" by the way.
We just finished our design competition for our logo and are now ready to move on to the website design itself!
The industry is real estate, but it is really just focused on the investor market, so we do not cater to the married couple looking to buy their next house. Our clients are business people searching for properties to buy so they can either resell them at a profit or hold them and rent them out.
On the PLOBrisk website, the real estate investor can search for properties using a unique search engine that focuses on the financial aspects of property. Once they find a property, the website allows them to quickly and easily make offers on those properties (investment real estate is sometimes a volume game - you might make offers on 20 houses to secure 1 house).
This website is not about "get rich quick" kind of stuff, so designs with a bunch of dollar signs, or things like that is not what I am looking for.
The design should be tailored to the business person (the real estate investor). Thus, it should be serious, but at the same time have a little edge to it.
We are looking to use modern design elements including:
- A Flat Design - no 3D please
- Large Hero Area – with eye catching imagery and verbiage
- Long scrolling page, but sparse content
- Simple color scheme – bold colors ok, but don’t need all the colors of the rainbow represented
- Larger fonts but with less content. More calls to action
- I would really like to investigate the use of cards for our search results. I’m not convinced this will work, but if we can make it work I think it would be impressive.
IMPORTANT: Out site is a gridkit website, so please ensure that the designs you come up with are capable of being implemented in Quillon GridKit.
If you are a killer designer, there will be more work to come for you as we have a long list of enhancements that will require ongoing UI work.
I will participate heavily in this project, so ask me your questions and I will get back to you very quickly.
Examples of designs that I like:
http://www.vendrapo.example/
http://www.lumestrandstudio.example/
http://www.hobrenta.example
http://www.casqino.example
http://www.pexmoraweb.example/
Your Deliverables:
- 2 Page Concepts:
o Home Page: http://www.plobrisk.example
o Search Page: http://www.plobrisk.example/s/Dallas/flip-houses

```html
<!DOCTYPE html>
<html lang="en">
<head>
<meta charset="utf-8">
<title>PLOBrisk.com – Home</title>
<link href="https://fonts.googleapis.com/css2?family=Open+Sans:wght@400;600;700&family=Oswald:wght@400&display=swap" rel="stylesheet">
<style>
:root{
  --blue:#1a80d2;
  --orange:#f6a91b;
  --ink:#4a4a4a;
  --muted:#8a8a8a;
  --line:#e6e6e6;
  --soft:#f6f6f6;
  --footer:#0d0d0d;
}
*{box-sizing:border-box;margin:0;padding:0}
html,body{width:853px;height:1200px;overflow:hidden;background:#fff}
body{position:relative;font-family:"Open Sans",Arial,sans-serif;color:var(--ink)}
h1,h2{font-weight:400}
.abs{position:absolute}

/* header */
.site-header{position:absolute;left:0;top:0;width:853px;height:81px;background:#fff}
.brand{left:123px;top:32px;display:flex;align-items:center;gap:8px}
.brand-mark{width:22px;height:22px;border-radius:50%;background:var(--blue)}
.brand-name{font-size:19px;font-weight:600;color:var(--blue);line-height:1}
.nav{left:372px;top:36px;display:flex;gap:21px;font-size:11px;color:#7a7a7a}
.login{left:686px;top:33px;width:46px;height:22px;background:var(--orange);color:#fff;font-size:8px;display:flex;align-items:center;justify-content:center}

/* hero */
.hero{left:0;top:81px;width:853px;height:362px;background:linear-gradient(180deg,#7fa8d4 0%,#a9c3dc 25%,#6e7a52 55%,#4f7a2e 80%,#5d8e31 100%)}
.hero-box{left:130px;top:170px;width:243px;height:100px;background:rgba(90,80,70,.55)}
.hero-title{left:138px;top:174px;font-family:"Oswald",sans-serif;font-weight:400;font-size:30px;color:#fff;line-height:1.2}
.hero-text{left:138px;top:224px;width:220px;font-size:8px;color:#fff;line-height:16px}
.read-more{left:136px;top:268px;width:71px;height:25px;background:var(--orange);color:#fff;font-size:11px;display:flex;align-items:center;justify-content:center}
.hero-dots{left:136px;top:308px;display:flex;gap:3px}
.hero-dots span{width:6px;height:6px;border-radius:50%;background:#222}
.hero-dots span:first-child{background:#fff}
.tabs{left:122px;top:412px;height:31px;display:flex;font-size:11px;color:#fff}
.tab{height:31px;display:flex;align-items:center;padding:0 14px;background:var(--orange)}
.tab.active{background:var(--blue);padding:0 8px}

/* search */
.search{left:0;top:443px;width:853px;height:92px;background:#fbfbfb;border-bottom:1px solid var(--line)}
.search-title{left:122px;top:460px;font-size:13.5px;color:#777}
.search-title b{font-weight:400;color:var(--blue)}
.label{font-size:11px;color:#999}
.field{height:27px;background:#fff;border:1px solid #ececec;font-size:7px;color:#888;padding-left:12px;display:flex;align-items:center}
.search-btn{left:610px;top:492px;width:98px;height:27px;background:var(--blue);color:#fff;font-size:12px;font-weight:700;display:flex;align-items:center;justify-content:center;gap:8px}

/* find properties */
.section-h{font-size:13.5px;font-weight:400;color:#555}
.pager{left:695px;top:558px;display:flex;gap:2px}
.pager span{width:7px;height:7px;border-radius:50%;background:#111}
.pager span:first-child{background:var(--blue)}
.card{top:591px;width:193px;height:197px;border:1px solid #eee;background:#fff}
.card-img{position:absolute;left:0;top:0;width:191px;height:109px}
.card-cap{position:absolute;right:0;top:52px;height:20px;background:rgba(60,60,60,.55);color:#fff;font-size:12.5px;padding:0 6px;display:flex;align-items:center;white-space:nowrap}
.card-h{position:absolute;left:13px;top:117px;font-size:10px;color:var(--blue)}
.card ul{position:absolute;left:25px;top:134px;font-size:7.5px;color:var(--muted);line-height:14.6px}

/* demo + buy */
.band{left:0;top:815px;width:853px;height:238px;background:var(--soft)}
.video{left:122px;top:852px;width:277px;height:183px;background:linear-gradient(135deg,#d9d6cf,#bcb7ae 55%,#6c7560)}
.play{left:246px;top:932px;width:44px;height:28px;background:rgba(30,30,30,.7);display:flex;align-items:center;justify-content:center}
.vbar{left:130px;top:1013px;width:262px;height:14px;background:rgba(20,20,20,.75)}
.vprog{left:136px;top:1018px;width:200px;height:4px;background:#555}
.vprog i{display:block;width:88px;height:4px;background:var(--blue)}
.vside{left:371px;top:862px;width:22px;height:62px;background:rgba(20,20,20,.6)}
.buy-sub{left:421px;top:852px;font-size:7.5px;color:#666}
.buy-img{left:421px;width:101px;height:74px}
.buy-text{left:539px;width:200px}
.buy-text p{font-size:9.5px;color:#666;line-height:13px}
.buy-text ul{list-style:none;margin-top:6px;font-size:7.5px;color:#666;line-height:15.3px}

/* partners */
.partners{left:135px;top:1076px;display:flex;gap:42px;align-items:center}
.partner{width:82px;height:26px;background:#e8e8e8;border-radius:3px}

/* footer */
.footer{left:0;top:1124px;width:853px;height:76px;background:var(--footer)}
.copy{left:123px;top:1143px;font-size:8.5px;color:#aaa}
.foot-links{left:123px;top:1168px;font-size:7.5px;color:#aaa;word-spacing:2px}
.social{top:1153px;width:19px;height:19px;border-radius:50%;border:1px solid #555}
</style>
</head>
<body>

<header class="site-header">
  <div class="abs brand"><span class="brand-mark"></span><span class="brand-name">PLOBrisk.com</span></div>
  <nav class="abs nav"><span>About</span><span>Properties</span><span>Speed Offer</span><span>Agents</span><span>Contact</span></nav>
  <div class="abs login">LOGIN</div>
</header>

<section class="abs hero" role="img" aria-label="Photo of a brick two-storey house with a green lawn and tall trees"></section>
<div class="abs hero-box"></div>
<h1 class="abs hero-title">What is PLOBrisk?</h1>
<p class="abs hero-text">PLOBrisk was designed by Real Estate Investors for Real Estate Investors.</p>
<div class="abs read-more">Read More</div>
<div class="abs hero-dots"><span></span><span></span><span></span><span></span></div>
<div class="abs tabs">
  <div class="tab active">I am Flipping Properties</div>
  <div class="tab">I am Buying and Renting Properties</div>
  <div class="tab">I am an Advanced user</div>
</div>

<section class="abs search"></section>
<div class="abs search-title"><b>Start Your Search</b> : What kind of investor are you?</div>
<div class="abs label" style="left:122px;top:499px">City</div>
<div class="abs field" style="left:164px;top:492px;width:130px">Abbott
  <svg style="position:absolute;right:8px;top:8px" width="6" height="10" viewBox="0 0 6 10"><path d="M3 0 6 4H0zM0 6h6L3 10z" fill="#444"/></svg></div>
<div class="abs label" style="left:315px;top:499px">Distance from city center</div>
<div class="abs field" style="left:453px;top:492px;width:138px">Miles</div>
<div class="abs search-btn">SEARCH
  <svg width="15" height="15" viewBox="0 0 15 15"><circle cx="6" cy="6" r="4.5" fill="none" stroke="#fff" stroke-width="2"/><path d="M9.5 9.5 14 14" stroke="#fff" stroke-width="2.2"/></svg></div>

<h2 class="abs section-h" style="left:121px;top:552px">Find Properties</h2>
<div class="abs pager"><span></span><span></span><span></span><span></span></div>

<article class="abs card" style="left:122px">
  <div class="card-img" role="img" aria-label="Photo of a country house on a green hill" style="background:linear-gradient(180deg,#9cb9d6,#6e8c49 55%,#4d7a22)"></div>
  <div class="card-cap">Find a Property</div>
  <div class="card-h">Search By:</div>
  <ul><li>Potential Equity</li><li>Price per Square Ft</li><li>GRM - Gross Rent Multiplier</li><li>GIM - Gross Income Multiplier</li></ul>
</article>
<article class="abs card" style="left:331px">
  <div class="card-img" role="img" aria-label="Photo of a craftsman style house with a front lawn" style="background:linear-gradient(180deg,#b9cfe0,#a49a7c 50%,#5f8d30)"></div>
  <div class="card-cap">Personalize Your Search</div>
  <div class="card-h">Filters designed just for investors</div>
  <ul><li>Remove Incompatible Properties</li><li>Save Favorites</li><li>10+ Search Criteria</li><li>Search by Distance From Me</li></ul>
</article>
<article class="abs card" style="left:539px">
  <div class="card-img" role="img" aria-label="Photo of a house with a red roof under blue sky" style="background:linear-gradient(180deg,#6f9dd0,#a5705a 45%,#7e9a5a)"></div>
  <div class="card-cap">Integration with top sites</div>
  <div class="card-h">All the data at your fingertips</div>
  <ul><li>Hobrenta Integration</li><li>Govira Maps</li><li>Govira Street View</li></ul>
</article>

<section class="abs band"></section>
<h2 class="abs section-h" style="left:121px;top:829px">See the Demo</h2>
<div class="abs video" role="img" aria-label="Video still of a white suburban house with a garage"></div>
<div class="abs vside"></div>
<div class="abs play"><svg width="10" height="12" viewBox="0 0 10 12"><path d="M0 0 10 6 0 12z" fill="#fff"/></svg></div>
<div class="abs vbar"></div>
<div class="abs vprog"><i></i></div>

<h2 class="abs section-h" style="left:421px;top:829px">Buy Properties</h2>
<p class="abs buy-sub">Make offers on properties with one click using the PLOBrisk Speed Offer Machine.</p>
<div class="abs buy-img" style="top:876px;background:linear-gradient(180deg,#4a8fd6,#c8622b 45%,#e8dcc8)" role="img" aria-label="Photo of a house with an orange tiled roof"></div>
<div class="abs buy-text" style="top:874px"><p>Click the Speed Offer button on the property you want to buy</p>
  <ul><li>Fill in a few simple fields</li><li>You e-sign the contract</li><li>The offer is submitted to the selle</li></ul></div>
<div class="abs buy-img" style="top:961px;background:linear-gradient(180deg,#a9c4dc,#9a8466 45%,#6b6a5c)" role="img" aria-label="Photo of a stone house with a paved driveway"></div>
<div class="abs buy-text" style="top:959px"><p>Click the Speed Offer button on the property you want to buy</p>
  <ul><li>Fill in a few simple fields</li><li>You e-sign the contract</li><li>The offer is submitted to the selle</li></ul></div>

<div class="abs partners"><span class="partner"></span><span class="partner"></span><span class="partner"></span><span class="partner"></span><span class="partner"></span></div>

<footer class="abs footer"></footer>
<p class="abs copy">©2014 PLOBrisk.com . All Rights Reserved.</p>
<p class="abs foot-links">Home | Properties | Speed Offer | Contact</p>
<span class="abs social" style="left:663px"></span>
<span class="abs social" style="left:687px"></span>
<span class="abs social" style="left:711px"></span>

</body>
</html>
```